Cardiology Practice needs Imaging Order Form

Busy Cardiology Practice needs an imaging order form for its various types of imaging services. A sample has been uploaded. Our primary colors are red, black and white. Design should be able to fit 8 1/2 by 11 paper. Would like order form on one side and minimally the map on the other side with our demographic information which is Coral Ridge Cardiac, PLLC located at 718 Tamber Ln. Ste. K, Harlow Creek, NM 87412. Phone is 713-264-8817, Fax is 713-264-8817, and our web address is coralridgecardiac.example. Our physicians names are Dorin Melvik, MD, G.L. Vombrasca, MD, Ottilie Granby, MD, Corwin Melvik, MD, and Leopold Danforth, MD. We also have 3 nurse practitioners whose names are Ruthie Marbeck, MSN, ACNP-BC, Delia Fairclough, MSN, APRN, AGNP-C and Minette Oakes, MSN, APRN, NP-C.

Target Market(s)

Healthcare

Industry/Entity Type

Healthcare

Font styles to use
Serif

Colors
ec1f27

Requirements
Must have
• All testing on sample order form uploaded. Clinic Logo, Map, Demographic Information, physician and nurse practitioner information and website.
Nice to have
• Open to suggestions
Should not have
• physician or nurse practitioner pictures

```html
<!DOCTYPE html>
<html lang="en">
<head>
<meta charset="utf-8">
<title>Imaging Service Requisition – Coral Ridge Cardiac</title>
<link rel="stylesheet" href="https://fonts.googleapis.com/css2?family=PT+Sans:wght@400;700&display=swap">
<style>
  :root {
    --red: #c1272d;
    --red-bright: #ec1f27;
    --black: #0d0d0d;
    --ink: #1e1e1e;
    --rule: #2b2b2b;
    --band: #e6e6e6;
    --bar-grey: #58595b;
    --paper: #ffffff;
    --backdrop: #ecebea;
  }
  * { box-sizing: border-box; margin: 0; padding: 0; }
  html, body { width: 1200px; height: 800px; overflow: hidden; }
  body { background: var(--backdrop); font-family: "PT Sans", sans-serif; color: var(--ink); position: relative; }

  .sheet { position: absolute; left: 294px; top: 4px; width: 613px; height: 792px; background: var(--paper); box-shadow: 0 2px 8px rgba(0,0,0,.15); overflow: hidden; }
  .sheet > * { position: absolute; }
  .decor { left: 0; top: 0; width: 613px; height: 792px; }

  .brand { left: 28px; top: 38px; display: flex; align-items: center; gap: 9px; color: #fff; font-weight: 700; font-size: 17px; letter-spacing: .3px; }
  .brand-dot { width: 26px; height: 26px; border-radius: 50%; border: 2.5px solid #fff; }

  .title { left: 336px; top: 9px; color: #fff; font-weight: 700; font-size: 30px; letter-spacing: -.2px; }

  .requisition { left: 371px; top: 66px; width: 207px; font-size: 8.5px; }
  .requisition .req-head { color: var(--red-bright); padding-bottom: 1px; border-bottom: 1px solid var(--rule); }
  .requisition .req-row { height: 14.5px; padding-top: 2px; border-bottom: 1px solid var(--rule); }

  .physicians { left: 18px; top: 146px; width: 561px; height: 29px; background: var(--red); border-radius: 12px 12px 0 0; color: #fff; font-weight: 700; font-size: 10px; display: flex; justify-content: center; align-items: center; gap: 10px; }

  .band { height: 14px; background: var(--band); font-weight: 700; font-size: 8.5px; padding: 1px 2px; }
  .band.center { text-align: center; }
  .label { font-size: 8.5px; white-space: nowrap; }
  .rule { height: 0; border-bottom: 1px solid var(--rule); }
  .choice { height: 15px; border: 1px solid var(--rule); font-size: 8.5px; text-align: center; line-height: 13px; width: 30px; }

  .notice { left: 18px; top: 420px; width: 561px; height: 15px; background: var(--bar-grey); color: #fff; font-size: 8.4px; line-height: 15px; padding-left: 19px; }

  .checklist { font-size: 8.5px; }
  .checklist li { list-style: none; height: 14.6px; line-height: 14.6px; }
  .checklist li.indent { padding-left: 12px; }
  .boxes { width: 22px; border: 1px solid #777; }
  .boxes span { display: block; height: 14.6px; border-bottom: 1px solid #777; }
  .boxes span:last-child { border-bottom: 0; }

  .firm { left: 17px; top: 753px; color: var(--red-bright); font-weight: 700; font-size: 11px; }
  .visit { left: 17px; top: 767px; color: #fff; font-size: 8.8px; }
  .contact-line { top: 770px; color: #fff; font-size: 10px; display: flex; align-items: center; gap: 6px; }
</style>
</head>
<body>
<main class="sheet">
  <svg class="decor" viewBox="0 0 613 792" aria-hidden="true">
    <path d="M225 0 H613 V60 H372 C330 60 300 40 280 22 C262 6 245 0 225 0 Z" fill="var(--black)"/>
    <path d="M0 0 H240 C280 0 300 30 325 48 C345 60 360 62 372 62 C352 70 340 90 310 100 C298 104 285 105 270 105 H0 Z" fill="var(--red)"/>
    <path d="M0 735 H300 C322 735 334 748 345 763 H613 V792 H0 Z" fill="var(--black)"/>
    <path d="M318 763 H613 V792 H305 C312 785 315 772 318 763 Z" fill="var(--red)"/>
  </svg>

  <div class="brand"><span class="brand-dot"></span><span>Coral Ridge Cardiac</span></div>
  <h1 class="title">IMAGING SERVICE</h1>

  <div class="requisition">
    <div class="req-head">Service requisition</div>
    <div class="req-row">Date:</div>
    <div class="req-row">Time:</div>
    <div class="req-row">Solicitor:</div>
  </div>

  <div class="physicians">
    <span>Dorin Melvik, M.D.</span><span>|</span>
    <span>G.L. Vombrasca, M.D.</span><span>|</span>
    <span>Ottilie Granby, M.D.</span><span>|</span>
    <span>Corwin Melvik, M.D.</span><span>|</span>
    <span>Leopold Danforth, M.D.</span>
  </div>

  <div class="band" style="left:18px;top:180px;width:254px">Patient information</div>
  <span class="label" style="left:19px;top:203px">Last name</span>
  <span class="label" style="left:123px;top:203px">First name</span>
  <span class="label" style="left:226px;top:203px">MI</span>
  <div class="rule" style="left:18px;top:230px;width:254px"></div>
  <span class="label" style="left:19px;top:247px">Date of birth</span>
  <div class="rule" style="left:18px;top:274px;width:103px"></div>
  <span class="label" style="left:175px;top:247px">Sex</span>
  <div class="choice" style="left:183px;top:259px">M</div>
  <div class="choice" style="left:232px;top:259px">F</div>

  <div class="band" style="left:324px;top:180px;width:255px">Contact information</div>
  <span class="label" style="left:326px;top:203px">Address</span>
  <div class="rule" style="left:324px;top:230px;width:255px"></div>
  <span class="label" style="left:325px;top:247px">Home phone no.</span>
  <div class="rule" style="left:324px;top:274px;width:103px"></div>
  <span class="label" style="left:478px;top:247px">Mobile phone no.</span>
  <div class="rule" style="left:478px;top:274px;width:101px"></div>

  <div class="band center" style="left:18px;top:289px;width:254px">Medical information</div>
  <span class="label" style="left:56px;top:305px">ICD-10</span>
  <span class="label" style="left:122px;top:305px">Narrative diagnosis</span>
  <span class="label" style="left:19px;top:319px">1.-</span>
  <div class="rule" style="left:18px;top:331px;width:254px"></div>
  <span class="label" style="left:19px;top:334px">2.-</span>
  <div class="rule" style="left:18px;top:346px;width:254px"></div>
  <span class="label" style="left:19px;top:349px">3.-</span>
  <div class="rule" style="left:18px;top:361px;width:254px"></div>

  <div class="band center" style="left:324px;top:289px;width:255px">Insurance information</div>
  <span class="label" style="left:325px;top:305px">Primary insurance</span>
  <span class="label" style="left:478px;top:305px">Suscribers no.</span>
  <div class="rule" style="left:324px;top:332px;width:255px"></div>
  <span class="label" style="left:325px;top:334px">Authorization required?</span>
  <div class="choice" style="left:336px;top:346px">Yes</div>
  <div class="choice" style="left:386px;top:346px">No</div>
  <span class="label" style="left:478px;top:334px">Authorization no.</span>
  <div class="rule" style="left:478px;top:361px;width:101px"></div>

  <span class="label" style="left:19px;top:377px">Prescriber's name</span>
  <div class="rule" style="left:18px;top:404px;width:103px"></div>
  <span class="label" style="left:174px;top:377px">Signature</span>
  <div class="rule" style="left:172px;top:404px;width:100px"></div>
  <span class="label" style="left:325px;top:377px">Fax no.</span>
  <div class="rule" style="left:324px;top:404px;width:103px"></div>
  <span class="label" style="left:478px;top:377px">STAT</span>
  <div class="choice" style="left:489px;top:389px">Yes</div>
  <div class="choice" style="left:538px;top:389px">No</div>

  <div class="notice">READ FIRST: Please check any that apply and attach referral if available. The patient will be contacted for further instructions.</div>

  <div class="band" style="left:18px;top:439px;width:254px">&nbsp;Electrophysiology</div>
  <ul class="checklist" style="left:21px;top:457px">
    <li>Electrocardiograms (EKG)</li>
    <li>Holter monitor (specify number of days: 3-14)</li>
    <li>Implantable loop recorder placement</li>
    <li>Implantable loop recorder monitoring</li>
    <li>Pacemaker check</li>
    <li>Pacemaker monitoring</li>
    <li>Internal cardiac defibrillator (ICD) check</li>
    <li>Internal cardiac defibrillator (ICD) monitoring</li>
  </ul>
  <div class="boxes" style="left:249px;top:456px"><span></span><span></span><span></span><span></span><span></span><span></span><span></span><span></span></div>

  <div class="band" style="left:18px;top:588px;width:254px">Cardiac stress test</div>
  <ul class="checklist" style="left:21px;top:609px"><li>stress test with echocardiogram</li></ul>
  <div class="boxes" style="left:249px;top:608px"><span></span></div>

  <div class="band" style="left:18px;top:632px;width:254px">Cardiac imaging</div>
  <ul class="checklist" style="left:21px;top:647px">
    <li>Echocardiogram</li>
    <li>Echocardiogram with bubble study</li>
    <li>Calcium score (Heart scan)</li>
    <li>Cardiac PET-CT</li>
  </ul>
  <div class="boxes" style="left:249px;top:649px"><span></span><span></span><span></span><span></span></div>

  <div class="band" style="left:324px;top:439px;width:255px">&nbsp;Vascular imaging</div>
  <ul class="checklist" style="left:330px;top:457px">
    <li>Carotid doppler</li>
    <li>Arterial doppler</li>
    <li class="indent">Upper extremities</li>
    <li class="indent">Lower extremities</li>
    <li class="indent">Abdominal aorta</li>
    <li class="indent">Renal arteries</li>
    <li>Venous doppler of the lower extremities (LE)</li>
    <li>Venous doppler of the LE with reflux study</li>
    <li>Enhanced external counter pulsation (EECP)</li>
    <li>PulseLink heart failure monitoring</li>
    <li>Home sleep study</li>
  </ul>
  <div class="boxes" style="left:557px;top:456px"><span></span><span></span><span></span><span></span><span></span><span></span><span></span><span></span><span></span><span></span><span></span></div>

  <div class="band" style="left:324px;top:632px;width:255px">&nbsp;Other unlisted procedures or special instructions:</div>
  <div class="rule" style="left:324px;top:665px;width:255px"></div>
  <div class="rule" style="left:324px;top:685px;width:255px"></div>
  <div class="rule" style="left:324px;top:706px;width:255px"></div>

  <div class="firm">Coral Ridge Cardiac, PLLC.</div>
  <div class="visit">Visit us at 718 Tamber Ln. Ste. K, Harlow Creek, NM 87412.</div>
  <div class="contact-line" style="left:340px">
    <svg width="9" height="9" viewBox="0 0 24 24" aria-hidden="true"><path fill="#fff" d="M6.6 10.8a15.1 15.1 0 0 0 6.6 6.6l2.2-2.2c.3-.3.7-.4 1-.2 1.1.4 2.3.6 3.6.6.6 0 1 .4 1 1V20c0 .6-.4 1-1 1A17 17 0 0 1 3 4c0-.6.4-1 1-1h3.5c.6 0 1 .4 1 1 0 1.3.2 2.5.6 3.6.1.3 0 .7-.2 1z"/></svg>
    <span>(713) 264-8817</span>
  </div>
  <div class="contact-line" style="left:448px">
    <svg width="9" height="9" viewBox="0 0 24 24" aria-hidden="true"><g fill="none" stroke="#fff" stroke-width="2"><circle cx="12" cy="12" r="10"/><path d="M2 12h20M12 2c3 3 3 17 0 20M12 2c-3 3-3 17 0 20"/></g></svg>
    <span>www.coralridgecardiac.example</span>
  </div>
</main>
</body>
</html>
```